Buch-/E-Book-Cover für Edelmetallberater
Zielgruppe
Zielgruppe sind Privatpersonen. Soll möglichst viele ansprechen, zeitgerecht und attraktiv wirken.
Ich selbst bin Edelmetallberater. Ziel ist es aufzuklären und gleichzeitig Neukunden zu gewinnen
Aufgabenstellung
Es soll attraktiv und zeitgerecht sein.
Die Bilder der Frontseite sind ein Vorschlag. Muss aber nicht so sein. Die Bilder sind von lumafoto und ich kann sie im Original liefern. Rückseite habe ich noch keinen Vorschlag. Freie Gestaltung.
Ich brauche ein fertiges Cover für ein Vendora ebook und die print Version bei Vendora

```html
<!DOCTYPE html>
<html lang="de">
<head>
<meta charset="utf-8">
<title>So schützen Sie Ihr Geld mit Gold – Buchumschlag</title>
<link rel="stylesheet" href="https://fonts.googleapis.com/css2?family=Oswald:wght@300;400;500;600;700&family=Roboto+Condensed:wght@400;700&display=swap">
<style>
  :root {
    --page: #ffffff;
    --cover: #050505;
    --gold: #e0b04a;
    --gold-dark: #a8741c;
    --white: #ffffff;
    --text-soft: #d9d9d9;
    --photo: #f2f2f4;
    --code-box: #8c8489;
  }
  html, body { margin: 0; padding: 0; overflow: hidden; background: var(--page); }
  .canvas { position: relative; width: 1200px; height: 1200px; background: var(--page); overflow: hidden; }
  .cover { position: absolute; left: 90px; top: 234px; width: 1020px; height: 732px; background: var(--cover); }

  /* back cover */
  .back { position: absolute; left: 0; top: 0; width: 474px; height: 732px; font-family: "Roboto Condensed", sans-serif; }
  .back-heading { position: absolute; left: 61px; top: 68px; margin: 0; font-family: "Oswald", sans-serif; font-weight: 600; font-size: 17px; color: var(--gold); }
  .benefit-list { position: absolute; left: 62px; top: 103px; width: 380px; margin: 0; padding: 0; list-style: none; }
  .benefit-list li { position: relative; padding-left: 20px; font-size: 10.5px; line-height: 13px; color: var(--text-soft); margin-bottom: 7px; }
  .benefit-list li::before { content: "\2713"; position: absolute; left: 0; top: 0; color: var(--gold); font-size: 11px; }
  .quote-rule { position: absolute; left: 60px; width: 370px; height: 1px; background: var(--gold-dark); }
  .quote { position: absolute; left: 40px; top: 364px; width: 410px; margin: 0; text-align: center; font-family: "Oswald", sans-serif; font-weight: 600; font-size: 19.5px; line-height: 28px; color: var(--gold); }
  .author-photo { position: absolute; left: 61px; top: 458px; width: 97px; height: 100px; background: var(--photo); }
  .author-name { position: absolute; left: 170px; top: 456px; margin: 0; font-family: "Oswald", sans-serif; font-weight: 600; font-size: 12px; color: var(--gold); }
  .author-bio { position: absolute; left: 170px; top: 474px; width: 272px; margin: 0; font-size: 10px; line-height: 13.8px; color: var(--text-soft); }
  .code-box { position: absolute; left: 311px; top: 617px; width: 159px; height: 65px; background: var(--code-box); }

  /* spine */
  .spine { position: absolute; left: 474px; top: 0; width: 66px; height: 732px; }
  .spine-title { position: absolute; left: 33px; top: 261px; transform: translate(-50%, -50%) rotate(90deg); white-space: nowrap; font-family: "Oswald", sans-serif; font-weight: 600; font-size: 17.5px; letter-spacing: 0.3px; color: var(--gold); }
  .spine-author { position: absolute; left: 33px; top: 582px; transform: translate(-50%, -50%) rotate(90deg); white-space: nowrap; font-family: "Oswald", sans-serif; font-weight: 400; font-size: 13px; letter-spacing: 5px; color: var(--white); }

  /* front cover */
  .front { position: absolute; left: 540px; top: 0; width: 480px; height: 732px; }
  .front svg { position: absolute; left: 0; top: 0; }
  .key-visual { position: absolute; left: 54px; top: 330px; width: 396px; height: 264px; border-radius: 6px;
    background: radial-gradient(ellipse at 48% 45%, #f3c956 0%, #c9862a 22%, #a14818 38%, rgba(150,160,150,0.85) 55%, rgba(120,130,125,0.6) 75%, rgba(5,5,5,0) 100%); }
  .front-author { position: absolute; left: 0; top: 680px; width: 480px; margin: 0; text-align: center; font-family: "Oswald", sans-serif; font-weight: 500; font-size: 25px; letter-spacing: 6px; color: var(--gold); }
</style>
</head>
<body>
<div class="canvas">
  <div class="cover">

    <section class="back">
      <h2 class="back-heading">Das erwartet Sie in diesem Buch:</h2>
      <ul class="benefit-list">
        <li>Wie Sie Ihr Erspartes in unsicheren Zeiten schützen.</li>
        <li>Wie Gold den Wert Ihres Geldes bewahrt.</li>
        <li>Praktische Hinweise zum klugen Goldkauf (für alle).</li>
        <li>Woher unser Geld kommt und warum Gold dabei zählt.</li>
        <li>Die Geschichte des ältesten Zahlungsmittels.</li>
        <li>Warum die weltweite Verschuldung den Goldpreis bewegt.</li>
        <li>Was Silber, Platin und Palladium auszeichnet.</li>
        <li>Wissenswertes über Anlagen in seltene Industriemetalle.</li>
        <li>Wie Sie mit kleinen Beträgen ein Vermögen schaffen.</li>
        <li>Was Sparbuch, Festgeld und klassische Versicherungen heute wirklich leisten können.</li>
        <li>Sachwerte im Vergleich: Immobilien oder Edelmetalle.</li>
      </ul>
      <div class="quote-rule" style="top:350px"></div>
      <p class="quote">„Bei Gold zählt nicht der aktuelle Kurs,<br>sondern dass Sie es in Händen halten“.</p>
      <div class="quote-rule" style="top:426px"></div>
      <div class="author-photo" role="img" aria-label="Porträtfoto des Autors"></div>
      <h3 class="author-name">LUKAS DERNING</h3>
      <p class="author-bio">Geboren 1976 im Allgäu. Fast zwei Jahrzehnte arbeitete er im Bankwesen, bevor er sich bewusst für einen neuen Weg entschied. Heute berät er als selbstständiger Edelmetallexperte, hält Vorträge und begleitet Privatanleger. In diesem Ratgeber erklärt er verständlich, wie man Ersparnisse mit Edelmetallen schützt und wie Geld, Inflation und Gold zusammenhängen. Sein Anliegen ist es, Menschen zu mehr finanzieller Freiheit zu führen. Lukas Derning lebt mit seiner Frau, zwei Söhnen und einer Katze am See.</p>
      <div class="code-box"></div>
    </section>

    <section class="spine">
      <div class="spine-title">SO SCHÜTZEN SIE IHR GELD MIT GOLD</div>
      <div class="spine-author">LUKAS DERNING</div>
    </section>

    <section class="front">
      <div class="key-visual" role="img" aria-label="Goldbarren auf einem brennenden Geldschein"></div>
      <svg width="480" height="732" viewBox="0 0 480 732">
        <defs>
          <linearGradient id="gold-title" x1="0" y1="0" x2="0" y2="1">
            <stop offset="0" stop-color="#f8e08e"/>
            <stop offset="0.5" stop-color="#d9a53f"/>
            <stop offset="1" stop-color="#9c6a1c"/>
          </linearGradient>
          <radialGradient id="seal-gold" cx="0.4" cy="0.35" r="0.7">
            <stop offset="0" stop-color="#f5d27a"/>
            <stop offset="1" stop-color="#a8741c"/>
          </radialGradient>
        </defs>
        <g font-family="Oswald, sans-serif" font-weight="700">
          <text x="68" y="114" font-size="66" fill="#ffffff" textLength="336" lengthAdjust="spacingAndGlyphs">SO SCHÜTZEN SIE</text>
          <text x="52" y="180" font-size="66" fill="url(#gold-title)" textLength="370" lengthAdjust="spacingAndGlyphs">IHR GELD MIT GOLD</text>
          <text x="52" y="240" font-size="62" fill="#ffffff" textLength="370" lengthAdjust="spacingAndGlyphs">IN JEDER KRISE</text>
        </g>
        <line x1="52" y1="252" x2="422" y2="252" stroke="#a8741c" stroke-width="1"/>
        <text x="237" y="279" text-anchor="middle" font-family="Oswald, sans-serif" font-weight="300" font-size="20" fill="#e0b04a" textLength="362" lengthAdjust="spacingAndGlyphs">IHR PRAKTISCHER LEITFADEN FÜR UNSICHERE ZEITEN</text>
        <line x1="52" y1="286" x2="422" y2="286" stroke="#a8741c" stroke-width="1"/>

        <g class="seal" transform="translate(364 588)">
          <circle r="62" fill="url(#seal-gold)" stroke="#8a5a14" stroke-width="6" stroke-dasharray="3 3"/>
          <circle r="54" fill="#0a0a0a"/>
          <circle r="54" fill="none" stroke="#e0b04a" stroke-width="2"/>
          <g font-family="Oswald, sans-serif" text-anchor="middle" fill="#ffffff">
            <text y="-20" font-size="16" font-weight="700">MIT EXTRA</text>
            <text y="-5" font-size="8" font-weight="600">SILBER, PLATIN, PALLADIUM,</text>
            <text y="6" font-size="8" font-weight="600">INDUSTRIEMETALLEN</text>
            <text y="17" font-size="8" font-weight="600">UND</text>
            <text y="28" font-size="8" font-weight="600">DIGITALWÄHRUNGEN</text>
          </g>
        </g>
      </svg>
      <p class="front-author">LUKAS DERNING</p>
    </section>

  </div>
</div>
</body>
</html>
```